Meridane Partners Web Site

I would like to change our current website to a better design. www.meridanepartners.net.
Use the content from the this website.
Updates
The web site is down until 7AM EST on 3/25 for server maintenance. Sorry for the inconvenience.
REMEMBER: I am changing the website to focus on science and technical jobs across all industries. So, if your images focus on only biotech or only DNA or beakers that will not serve Aerospace very well or curcuit board manufacturing. So, either use a montage of images that cover everything or make you images more abstract.
Target Market(s)
We are now staffing for all science and technical jobs. Not just biotech and pharmaceutical.
So, pharmaceutical, biotech, aerospace, alternative energy, research, medical...etc. Anyone with a science or tehcnical background.
Number of Pages Required
5+ pages
Requirements
Must have
- Tag line: "The Science of Recruiting" replaces "A pharmaceutical and bitech search firm"
Pictures and images across more industries.
The job serach page only needs a banner. That page is being worked internally.

```html
<!DOCTYPE html>
<html lang="en">
<head>
<meta charset="utf-8">
<title>Meridane Partners – The Science of Recruiting</title>
<link rel="stylesheet" href="https://fonts.googleapis.com/css2?family=Jost:wght@400;500&family=Open+Sans:wght@400;600;700&family=Noto+Sans:wght@700&display=swap">
<style>
  :root{
    --green:#1d4a1e;
    --gold:#c27a16;
    --ink:#333;
    --ink-soft:#555;
    --bar:#2b2b2b;
    --nav-ink:#4a4a4a;
    --panel-line:#d8d8d8;
  }
  *{box-sizing:border-box;margin:0;padding:0}
  html,body{width:1150px;height:1200px;overflow:hidden}
  body{
    position:relative;
    background:linear-gradient(#f0f0f0 0,#f2f2f2 500px,#fbfbfb 900px,#fff 1170px);
    font-family:"Open Sans",Verdana,sans-serif;
    color:var(--ink);
  }
  .abs{position:absolute}

  /* top bar */
  .topbar{left:0;top:0;width:1150px;height:29px;background:var(--bar)}
  .topband{left:0;top:30px;width:1150px;height:11px;background:#e2e2e2}
  .search-label{left:794px;top:8px;font:700 11px "Open Sans",sans-serif;color:#aaa;letter-spacing:.3px}
  .search-box{left:849px;top:4px;width:172px;height:19px;border-radius:10px;background:#fff}
  .search-box svg{position:absolute;right:5px;top:2px}

  /* brand */
  .brand{left:132px;top:100px;font:500 25px "Jost",sans-serif;color:var(--green);letter-spacing:.5px;text-transform:uppercase}
  .tagline{right:130px;top:104px;font:400 17px "Jost",sans-serif;color:var(--ink-soft);letter-spacing:1.5px;text-transform:uppercase}

  /* nav */
  .nav{left:128px;top:174px;width:892px;height:42px;border-radius:7px;background:linear-gradient(#fbfbfb,#e9e9e9);border:1px solid #dcdcdc}
  .nav-home{left:150px;top:168px;width:57px;height:40px;border-radius:3px;background:linear-gradient(#d29a55,#a5631c);
    color:#fff;font:400 14px "Jost",sans-serif;text-align:center;line-height:44px}
  .nav-home::after{content:"";position:absolute;right:-6px;top:0;border-left:6px solid #7a4410;border-top:6px solid transparent}
  .nav-item{top:186px;font:400 13.5px "Jost",sans-serif;color:var(--nav-ink);transform:translateX(-50%);white-space:nowrap}
  .nav-sep{top:186px;font:400 14px "Jost",sans-serif;color:#666}

  /* carousel */
  .card{top:224px;width:214px;height:291px;border-radius:6px;background:linear-gradient(#fafafa,#ebebeb);border:1px solid #e4e4e4;box-shadow:0 0 0 3px #fff}
  .card-photo{position:absolute;left:6px;top:6px;width:202px;height:207px;border-radius:3px}
  .card-title{position:absolute;left:0;width:100%;top:221px;text-align:center;font:400 14px "Jost",sans-serif;color:var(--green);line-height:16px;text-transform:uppercase}
  .card-text{position:absolute;left:0;width:100%;text-align:center;font:400 11px "Open Sans",sans-serif;color:#222;line-height:15px}
  .photo-solar{background:linear-gradient(160deg,#8fb3d8 0,#5c7fae 35%,#2d3f68 70%,#bcc7d8 100%)}
  .photo-genome{background:radial-gradient(circle at 40% 40%,#3e8fa8,#23647d 60%,#1b4f66)}
  .photo-clinic{background:linear-gradient(120deg,#eeeeec 0,#d9d6d0 45%,#c0a48a 75%,#8a5a3a 100%)}
  .photo-capsule{background:radial-gradient(circle at 45% 45%,#e1c850 0,#c9b05a 25%,#a9aaad 55%,#6e7075 100%)}

  .arrow{width:58px;height:58px;border-radius:50%;background:#fff;box-shadow:0 1px 3px rgba(0,0,0,.25);top:313px}
  .arrow svg{position:absolute;left:21px;top:20px}

  /* welcome */
  .welcome-title{left:132px;top:566px;font:400 28px "Jost",sans-serif;color:#444}
  .welcome-title .g{color:var(--green)} .welcome-title .o{color:var(--gold)}
  .welcome-sub{left:132px;top:625px;font:600 12px "Open Sans",sans-serif;color:#222;letter-spacing:.3px}
  .welcome-copy{left:132px;width:455px;font:400 11.7px/18.2px "Open Sans",sans-serif;color:#333;letter-spacing:.4px}

  .section-title{font:400 26px "Jost",sans-serif;color:#333}

  /* news */
  .news{left:130px;width:455px;border:1px solid #dadada;background:linear-gradient(90deg,#ececec,#f3f3f3)}
  .news-thumb{position:absolute;left:13px;top:8px;width:101px;height:67px;border:1px solid #ccc}
  .thumb-lab{background:linear-gradient(135deg,#d8eef3,#6fc8db 50%,#b4e0ea)}
  .thumb-molecule{background:radial-gradient(circle at 50% 45%,#555 0,#999 30%,#ddd 70%,#f3f3f3)}
  .news-head{position:absolute;left:122px;top:12px;font:700 12px "Open Sans",sans-serif;color:var(--green);letter-spacing:.4px}
  .news-head .date{font-weight:400;font-size:10.5px;color:#444;margin-left:10px;letter-spacing:.2px}
  .news-text{position:absolute;left:122px;top:37px;width:268px;font:400 10.5px/16px "Open Sans",sans-serif;color:#333;letter-spacing:.25px}
  .more{font:700 11px "Open Sans",sans-serif;color:#222;letter-spacing:.3px}

  /* proposals */
  .proposals{left:661px;top:563px;width:359px;height:500px;border:1px solid var(--panel-line);background:linear-gradient(#f4f4f4,#f8f8f8)}
  .proposals-intro{left:689px;top:623px;width:320px;font:400 11.7px/16.4px "Open Sans",sans-serif;color:#333;letter-spacing:.15px}
  .prop-head{left:689px;width:320px;padding-left:14px;font:700 11.5px/16.4px "Open Sans",sans-serif;color:#222;letter-spacing:.3px}
  .prop-head::before{content:"»";position:absolute;left:0;top:-1px}
  .prop-text{left:703px;width:300px;font:400 11.7px/16.4px "Open Sans",sans-serif;color:#333;letter-spacing:.15px}

  /* footer */
  .footer{left:0;top:1170px;width:1150px;height:30px;background:var(--bar)}
  .footer-copy{left:132px;top:1177px;font:700 9.6px "Noto Sans",sans-serif;color:#fff}
  .footer-links{right:129px;top:1177px;font:700 9.6px "Noto Sans",sans-serif;color:#fff;white-space:nowrap}
  .footer-links span{margin:0 6px}
</style>
</head>
<body>

<header>
  <div class="abs topbar"></div>
  <div class="abs topband"></div>
  <div class="abs search-label">SEARCH</div>
  <div class="abs search-box">
    <svg width="16" height="16" viewBox="0 0 16 16"><circle cx="6.5" cy="6.5" r="4.5" fill="none" stroke="#888" stroke-width="1.4"/><line x1="10" y1="10" x2="14" y2="14" stroke="#888" stroke-width="1.8"/></svg>
  </div>

  <div class="abs brand">Meridane Partners</div>
  <div class="abs tagline">The Science of Recruiting</div>

  <nav>
    <div class="abs nav"></div>
    <div class="abs nav-home">HOME</div>
    <span class="abs nav-sep" style="left:231px">|</span>
    <span class="abs nav-item" style="left:297px">ABOUT US</span>
    <span class="abs nav-sep" style="left:363px">|</span>
    <span class="abs nav-item" style="left:428px">EXPERTISE</span>
    <span class="abs nav-sep" style="left:491px">|</span>
    <span class="abs nav-item" style="left:587px">EMPLOYER SERVICES</span>
    <span class="abs nav-sep" style="left:683px">|</span>
    <span class="abs nav-item" style="left:783px">CANDIDATE SERVICES</span>
    <span class="abs nav-sep" style="left:880px">|</span>
    <span class="abs nav-item" style="left:951px">CONTACT US</span>
  </nav>
</header>

<section class="carousel">
  <div class="abs card" style="left:132px">
    <div class="card-photo photo-solar" role="img" aria-label="Solar panels against a blue sky"></div>
    <div class="card-title">Alternative Energy:</div>
    <div class="card-text" style="top:243px">Lorem Ipsum is simply<br>dummy text</div>
  </div>
  <div class="abs card" style="left:357px">
    <div class="card-photo photo-genome" role="img" aria-label="Blue DNA double helix"></div>
    <div class="card-title">Genomics</div>
    <div class="card-text" style="top:243px">Lorem Ipsum is simply<br>dummy text</div>
  </div>
  <div class="abs card" style="left:582px">
    <div class="card-photo photo-clinic" role="img" aria-label="Doctor consulting with a patient"></div>
    <div class="card-title">Clinical Research</div>
    <div class="card-text" style="top:243px">Lorem Ipsum is simply<br>dummy text</div>
  </div>
  <div class="abs card" style="left:808px">
    <div class="card-photo photo-capsule" role="img" aria-label="Yellow medicine capsules in a blister pack"></div>
    <div class="card-title" style="top:220px">Pharmaceutical<br>Manufacturing</div>
    <div class="card-text" style="top:254px">Lorem Ipsum is simply<br>dummy text</div>
  </div>

  <div class="abs arrow" style="left:105px">
    <svg width="16" height="18" viewBox="0 0 16 18"><path d="M12 1 L4 9 L12 17" fill="none" stroke="#222" stroke-width="4"/></svg>
  </div>
  <div class="abs arrow" style="left:990px">
    <svg width="16" height="18" viewBox="0 0 16 18"><path d="M4 1 L12 9 L4 17" fill="none" stroke="#222" stroke-width="4"/></svg>
  </div>
</section>

<main>
  <h1 class="abs welcome-title">Welcome to <span class="g">Meridane</span> <span class="o">Partners!</span></h1>
  <h2 class="abs welcome-sub">Executive Search, Recruiting and Contract Services</h2>
  <p class="abs welcome-copy" style="top:655px">Employees are every company’s key to success. Meridane Partners is a recruiting and search firm distinctly focused on those industries we know best. We have placed employees at all levels throughout the United States.</p>
  <p class="abs welcome-copy" style="top:728px">Our continued success and growth are a result of a consistent high level of service with unparalleled commitment to quality and integrity. We are a partner with our clients who rely on our network of candidates within the industry to help them achieve the next level of excellence.</p>

  <h2 class="abs section-title" style="left:131px;top:831px">Recent News:</h2>
  <article class="abs news" style="top:883px;height:82px">
    <div class="news-thumb thumb-lab" role="img" aria-label="Laboratory glassware with blue liquid"></div>
    <div class="news-head">Proposal 1: <span class="date">|&nbsp;&nbsp; March 3, 2010</span></div>
    <div class="news-text">Lorem Ipsum is simply dummy text of the printing and typesetting industry.</div>
  </article>
  <article class="abs news" style="top:980px;height:84px">
    <div class="news-thumb thumb-molecule" role="img" aria-label="Molecular model of connected spheres"></div>
    <div class="news-head">Proposal 2: <span class="date">|&nbsp;&nbsp; March 5, 2010</span></div>
    <div class="news-text">Lorem Ipsum is simply dummy text of the printing and typesetting industry.</div>
  </article>
  <div class="abs more" style="left:551px;top:1071px">More</div>

  <aside>
    <div class="abs proposals"></div>
    <h2 class="abs section-title" style="left:688px;top:567px">Our Proposals:</h2>
    <p class="abs proposals-intro">Lorem Ipsum is simply dummy text of the printing and typesetting industry. Lorem Ipsum has been the industry's standard dummy text ever since the 1500s.</p>

    <div class="abs prop-head" style="top:689px">Lorem Ipsum is simply dummy text of the printing and typesetting industry.</div>
    <p class="abs prop-text" style="top:738px">Lorem Ipsum has been the industry's standard dummy text ever since the 1500s.</p>
    <div class="abs more" style="left:944px;top:771px">More</div>

    <div class="abs prop-head" style="top:804px">Lorem Ipsum is simply dummy text of the printing and typesetting industry.</div>
    <p class="abs prop-text" style="top:853px">Lorem Ipsum has been the industry's standard dummy text ever since the 1500s.</p>
    <div class="abs more" style="left:944px;top:886px">More</div>

    <div class="abs prop-head" style="top:935px">Lorem Ipsum is simply dummy text of the printing and typesetting industry.</div>
    <p class="abs prop-text" style="top:984px">Lorem Ipsum has been the industry's standard dummy text ever since the 1500s.</p>
    <div class="abs more" style="left:944px;top:1017px">More</div>
  </aside>
</main>

<footer>
  <div class="abs footer"></div>
  <div class="abs footer-copy">Copyright 2005,Meridane Partners | All rights reserved</div>
  <div class="abs footer-links">Home<span>|</span>About Us<span>|</span>Employer Services<span>|</span>Candidate Services<span>|</span>Contact Us</div>
</footer>

</body>
</html>
```